Lomi-Seret - Promote and Support a community

Design a website for Ethiopean Community. the design should be friendly, easy to navigate and maintain the look & feel of the Ethiopian culture. a proposed logo is attached but it can be change according to your recommendations. This is a project we are doing at a discount rate as it supports a weak community.
Please visit their current website http://www.lomi-seret.example.il/index.php?lang=en

Target Market(s)

Community members, potential doners

Industry/Entity Type

community

Number of Pages Required

1 page

Font styles to use
Sans Serif

Requirements
Must have
• easy to navigate friendly interface

```html
<!DOCTYPE html>
<html lang="en">
<head>
<meta charset="utf-8">
<title>Lomi-Seret — Promote and Support a Community</title>
<link href="https://fonts.googleapis.com/css2?family=Figtree:wght@400;500;600;700;800&display=swap" rel="stylesheet">
<style>
  :root{
    --red:#8b0d0f;
    --red-deep:#7a0a0c;
    --ink:#1c1c1c;
    --text:#3a3a3a;
    --muted:#7a7a7a;
    --white:#ffffff;
    --navy:#141a26;
    --lilac:#f5f4fb;
    --lime:#c6dc8a;
    --line:#d6d6d6;
  }
  *{box-sizing:border-box;margin:0;padding:0}
  html,body{width:1200px;height:2913px;overflow:hidden;background:var(--white)}
  body{font-family:"Figtree",sans-serif;color:var(--ink);position:relative}
  .abs{position:absolute}

  /* header */
  .site-header{position:absolute;left:0;top:0;width:1200px;height:100px;background:var(--white)}
  .brand{position:absolute;left:80px;top:28px;display:flex;align-items:center;gap:10px}
  .brand-dot{width:40px;height:40px;border-radius:50%;background:var(--red)}
  .brand-name{font-size:20px;font-weight:700;color:var(--red)}
  .main-nav a{position:absolute;top:39px;font-size:16px;font-weight:500;color:var(--ink);text-decoration:none;white-space:nowrap}

  /* hero */
  .hero{position:absolute;left:0;top:100px;width:1200px;height:594px}
  .hero-title{position:absolute;left:160px;top:187px;font-size:44px;font-weight:800;color:#000;letter-spacing:-0.3px;white-space:nowrap}
  .btn-solid{position:absolute;background:var(--red);color:var(--white);font-weight:600;display:flex;align-items:center;justify-content:center;border-radius:20px}

  /* about */
  .about-rule{position:absolute;left:163px;top:863px;width:51px;height:3px;background:var(--red)}
  .about-text{position:absolute;left:163px;top:883px;font-size:14.5px;line-height:27.5px;color:var(--text);white-space:nowrap}
  .btn-outline{position:absolute;left:163px;top:1095px;width:147px;height:41px;border:1.5px solid var(--red);border-radius:21px;display:flex;align-items:center;justify-content:center;font-size:15px;font-weight:600;color:var(--ink)}

  /* services */
  .services-title{position:absolute;left:0;width:1200px;top:1385px;text-align:center;font-size:48px;font-weight:700;color:var(--white)}
  .services-lead{position:absolute;left:0;width:1200px;top:1451px;text-align:center;font-size:16.5px;line-height:27px;color:var(--white);white-space:nowrap}
  .service-card{position:absolute;background:var(--white);border-radius:4px;text-align:center}
  .service-card svg{display:block;margin:30px auto 0}
  .service-card h3{font-size:16px;font-weight:600;color:var(--red);margin-top:18px}
  .service-card p{font-size:11px;line-height:19.5px;color:var(--muted);margin-top:6px;white-space:nowrap}

  /* contact */
  .contact-title{position:absolute;left:0;width:1200px;top:2276px;text-align:center;font-size:31px;font-weight:800;color:#222}
  .contact-card{position:absolute;left:193px;top:2348px;width:813px;height:301px;background:var(--white);border-top:3px solid var(--red);border-radius:3px;box-shadow:0 2px 10px rgba(0,0,0,.06)}
  .contact-card h4{position:absolute;left:91px;top:24px;font-size:19px;font-weight:500;color:#333}
  .field{position:absolute;border:1px solid var(--line);border-radius:2px;font-size:10.5px;color:#9a9a9a;padding:10px 15px}
  .btn-submit{position:absolute;left:90px;top:239px;width:116px;height:30px;background:var(--red);color:var(--white);font-size:12px;font-weight:700;display:flex;align-items:center;justify-content:center}

  /* footer */
  .footer-nav a{position:absolute;top:2665px;font-size:15px;font-weight:500;color:var(--white);text-decoration:none;white-space:nowrap}
  .foot-col{position:absolute;top:2727px}
  .foot-col h5{font-size:12px;font-weight:700;color:var(--white);letter-spacing:.2px;padding-bottom:8px;border-bottom:1px solid #3a4150;width:156px}
  .foot-col ul{list-style:none;margin-top:8px}
  .foot-col li{font-size:11.5px;line-height:23.7px;color:#dfe2e8}
  .newsletter{position:absolute;left:827px;top:2727px}
  .newsletter h5{font-size:12px;font-weight:700;color:var(--white);padding-bottom:8px;border-bottom:1px solid #3a4150;width:179px}
  .newsletter p{font-size:11.5px;color:#dfe2e8;margin-top:13px}
  .nl-input{position:absolute;left:0;top:61px;width:107px;height:24px;background:var(--white)}
  .nl-btn{position:absolute;left:107px;top:61px;width:72px;height:24px;background:var(--red);color:var(--white);font-size:11px;display:flex;align-items:center;justify-content:center}
  .social{position:absolute;top:108px;width:20px;height:20px;border:1.5px solid var(--white);border-radius:50%}
</style>
</head>
<body>

<header class="site-header">
  <div class="brand"><span class="brand-dot"></span><span class="brand-name">Lomi-Seret</span></div>
  <nav class="main-nav">
    <a style="left:399px">Home</a>
    <a style="left:460px">About</a>
    <a style="left:526px">The Community</a>
    <a style="left:676px">Programs</a>
    <a style="left:765px">News</a>
    <a style="left:830px">Advocacy</a>
    <a style="left:932px">Partners</a>
    <a style="left:1027px">Support Us</a>
  </nav>
</header>

<section class="hero">
  <svg class="abs" style="left:0;top:0" width="1200" height="594" role="img" aria-label="Photo of colourful woven Ethiopian baskets with lids">
    <defs>
      <linearGradient id="heroFill" x1="0" y1="0" x2="1" y2="1">
        <stop offset="0" stop-color="#e9a6c8"/>
        <stop offset=".35" stop-color="#c04fa8"/>
        <stop offset=".6" stop-color="#7d5ad0"/>
        <stop offset=".8" stop-color="#e23a6a"/>
        <stop offset="1" stop-color="#3ea7d8"/>
      </linearGradient>
    </defs>
    <path d="M0 0H1200V530Q650 650 0 535Z" fill="url(#heroFill)"/>
  </svg>
  <h1 class="hero-title">Welcome to Lomi-Seret</h1>
  <div class="btn-solid" style="left:164px;top:300px;width:139px;height:39px;font-size:13px">LEARN MORE</div>
</section>

<section class="about">
  <svg class="abs" style="left:0;top:830px" width="70" height="300" aria-hidden="true">
    <circle cx="-80" cy="143" r="140" fill="var(--lilac)"/>
  </svg>
  <div class="about-rule"></div>
  <p class="about-text">Aliyah (immigration) from Ethiopia to Israel and the transition to a<br>sedentary lifestyle has resulted in the emergence of chronic<br>diseases, in particular diabetes. While only 0.4% of the new immi-<br>grants were diagnosed with Type 2 diabetes upon arrival, by the<br>time they had lived in Israel for ten years the figure had risen to<br>18% – three times as many as in the general population.&nbsp; The inci-<br>dence of hypertension, obesity, asthma and Type 1 diabetes had</p>
  <div class="btn-outline">Learn More</div>
  <svg class="abs" style="left:660px;top:770px" width="460" height="430" role="img" aria-label="Round photo of children gathered together at a community activity">
    <defs>
      <linearGradient id="kidsFill" x1="0" y1="0" x2="1" y2="1">
        <stop offset="0" stop-color="#8b7a86"/>
        <stop offset=".5" stop-color="#3b2f3e"/>
        <stop offset="1" stop-color="#2c3f8c"/>
      </linearGradient>
    </defs>
    <circle cx="214" cy="214" r="206" fill="url(#kidsFill)"/>
    <circle cx="375" cy="392" r="19" fill="none" stroke="var(--lime)" stroke-width="3"/>
    <circle cx="431" cy="398" r="11" fill="none" stroke="var(--lime)" stroke-width="2.5"/>
  </svg>
</section>

<section class="services">
  <svg class="abs" style="left:0;top:1268px" width="1200" height="945" role="img" aria-label="Deep red band over a photo of hands with a faint hexagon pattern">
    <defs>
      <linearGradient id="bandFill" x1="0" y1="0" x2="1" y2="1">
        <stop offset="0" stop-color="#a5393b"/>
        <stop offset=".55" stop-color="#953032"/>
        <stop offset="1" stop-color="#7e1719"/>
      </linearGradient>
    </defs>
    <path d="M0 100Q600 -60 1200 100V864Q600 1014 0 864Z" fill="url(#bandFill)"/>
    <path d="M0 100Q600 -60 1200 100" fill="none" stroke="var(--red-deep)" stroke-width="7"/>
    <path d="M0 864Q600 1014 1200 864" fill="none" stroke="var(--red-deep)" stroke-width="7"/>
  </svg>
  <h2 class="services-title">Services We Provide</h2>
  <p class="services-lead">Our business vision is to Plan, Track work to aim to Achieve success and results coordinating<br>support for Industries, Individuals, Organizations that includes.</p>

  <article class="service-card" style="left:163px;top:1545px;width:272px;height:240px">
    <svg width="72" height="72" viewBox="0 0 72 72" fill="var(--red)"><rect x="34" y="0" width="4" height="72"/><rect x="0" y="12" width="22" height="11" rx="2"/><rect x="0" y="40" width="22" height="11" rx="2"/><rect x="50" y="24" width="22" height="11" rx="2"/><rect x="50" y="52" width="22" height="11" rx="2"/><rect x="22" y="16" width="12" height="3"/><rect x="22" y="44" width="12" height="3"/><rect x="38" y="28" width="12" height="3"/><rect x="38" y="56" width="12" height="3"/></svg>
    <h3>Lorem Ipsum</h3>
    <p>Lorem Ipsum is simply dummy text of the<br>and typesetting industry. Lorem<br>been the industry's standard</p>
  </article>
  <article class="service-card" style="left:464px;top:1545px;width:272px;height:240px">
    <svg width="72" height="72" viewBox="0 0 72 72" fill="var(--red)"><rect x="0" y="0" width="22" height="22"/><rect x="50" y="0" width="22" height="22"/><rect x="0" y="50" width="22" height="22"/><rect x="50" y="50" width="22" height="22"/><path d="M28 11h14v-6l8 6-8 6v-6z"/><path d="M44 61H30v6l-8-6 8-6v6z"/><path d="M11 28v14H5l6 8 6-8h-6z"/><path d="M61 44V30h6l-6-8-6 8h6z"/></svg>
    <h3>Lorem Ipsum</h3>
    <p>Lorem Ipsum is simply dummy text of the<br>and typesetting industry. Lorem<br>been the industry's standard</p>
  </article>
  <article class="service-card" style="left:765px;top:1545px;width:272px;height:240px">
    <svg width="76" height="74" viewBox="0 0 76 74" fill="var(--red)"><circle cx="12" cy="10" r="8"/><circle cx="64" cy="10" r="8"/><circle cx="38" cy="34" r="8"/><rect x="20" y="8" width="36" height="4"/><path d="M0 70q0-18 12-22 12 4 12 22z"/><path d="M52 70q0-18 12-22 12 4 12 22z"/><path d="M26 60q0-14 12-16 12 2 12 16z"/><rect x="22" y="64" width="32" height="4"/></svg>
    <h3>Lorem Ipsum</h3>
    <p>Lorem Ipsum is simply dummy text of the<br>and typesetting industry. Lorem<br>been the industry's standard</p>
  </article>
  <article class="service-card" style="left:251px;top:1813px;width:335px;height:239px">
    <svg width="74" height="72" viewBox="0 0 74 72" fill="var(--red)"><circle cx="37" cy="12" r="10"/><circle cx="10" cy="20" r="6"/><circle cx="64" cy="20" r="6"/><path d="M2 32h14v16h-6v24H2z"/><path d="M58 32h14v40h-8V48h-6z"/><path d="M22 32h30v8H41v32h-8V40H22z"/></svg>
    <h3>Lorem Ipsum</h3>
    <p>Lorem Ipsum is simply dummy text of the<br>and typesetting industry. Lorem<br>been the industry's standard</p>
  </article>
  <article class="service-card" style="left:614px;top:1813px;width:335px;height:239px">
    <svg width="72" height="70" viewBox="0 0 72 70" fill="var(--red)"><circle cx="36" cy="9" r="9"/><circle cx="36" cy="61" r="9"/><circle cx="9" cy="35" r="9"/><circle cx="63" cy="35" r="9"/><path d="M14 22l8-8M50 14l8 8M58 48l-8 8M22 56l-8-8" stroke="var(--red)" stroke-width="3" fill="none"/><path d="M5 35l3 3 6-6M59 35l3 3 6-6" stroke="#fff" stroke-width="2" fill="none"/><rect x="31" y="6" width="10" height="2" fill="#fff"/><rect x="31" y="11" width="10" height="2" fill="#fff"/><rect x="31" y="58" width="10" height="2" fill="#fff"/><rect x="31" y="63" width="10" height="2" fill="#fff"/></svg>
    <h3>Lorem Ipsum</h3>
    <p>Lorem Ipsum is simply dummy text of the<br>and typesetting industry. Lorem<br>been the industry's standard</p>
  </article>
</section>

<svg class="abs" style="left:0;top:2520px" width="1200" height="393" role="img" aria-label="Dark footer backdrop with a faint mountain landscape">
  <path d="M0 12Q600 -40 1200 12V393H0Z" fill="var(--navy)"/>
</svg>

<section class="contact">
  <h2 class="contact-title">CONTACT</h2>
  <form class="contact-card">
    <h4>Feel Free to Contact Us</h4>
    <div class="field" style="left:90px;top:60px;width:310px;height:31px">First Name</div>
    <div class="field" style="left:414px;top:60px;width:309px;height:31px">Last Name</div>
    <div class="field" style="left:90px;top:104px;width:310px;height:30px">Email</div>
    <div class="field" style="left:414px;top:104px;width:309px;height:30px">Subject</div>
    <div class="field" style="left:90px;top:148px;width:633px;height:73px">Message...</div>
    <div class="btn-submit">SUBMIT</div>
  </form>
</section>

<footer>
  <nav class="footer-nav">
    <a style="left:163px">Home</a>
    <a style="left:218px">About</a>
    <a style="left:278px">The Community</a>
    <a style="left:416px">Programs</a>
    <a style="left:496px">News</a>
    <a style="left:555px">Advocacy</a>
    <a style="left:649px">Partners</a>
    <a style="left:735px">Support Us</a>
  </nav>
  <div class="foot-col" style="left:254px">
    <h5>SITELINKS</h5>
    <ul><li>Home</li><li>About Us</li><li>The Community</li><li>Programs</li></ul>
  </div>
  <div class="foot-col" style="left:511px">
    <h5>SITELINKS</h5>
    <ul><li>News</li><li>Advocacy</li><li>Partners</li><li>Support Us</li><li>Contact</li></ul>
  </div>
  <div class="newsletter">
    <h5>STAY IN TOUCH</h5>
    <p>Subscribe Our Newsletter</p>
    <div class="nl-input"></div>
    <div class="nl-btn">Subscribe</div>
    <span class="social" style="left:0"></span>
    <span class="social" style="left:25px"></span>
    <span class="social" style="left:50px"></span>
  </div>
</footer>

</body>
</html>
```